Business Card Design

Bowen therapy is a gentle therapy where moves are made(using your hands) over muscles or joint areas create myofascial release enabling the body to rebalance itself.

Its relaxing and have heal a variety of aliments . n contrast to other hands-on modalities, where the practitioner imposes correction on the client through manipulation, Bowen Technique facilitates the body in healing itself, with minimal intervention. Because of the subtle nature of Bowen Technique, and the body's continuing response to it over several days thereafter, other forms of manipulative therapy are discouraged for up to five days after a session, as they may interfere with the efficacy of the work.

Its an energy healing work using hands.
Its relaxing but professional.
I'm think of using blues, no greens or yellows. Some wave lines .

Target Market(s)

Anybody-

Industry/Entity Type

Business

Contact Information for Business Card

Maisie's Loxley Therapy,Maisie Corbett, Bowen Therapist,Cert IV Lumacore
Ashcombe, West Harrow Bay, Kelverton, 0417 905368,Gentle therapy restoring body balance.

Requirements
Must have
• Back needs a appointment table
with this wording :
Bowen Therapy is a subtle gentle bodywork therapy where a series of moves are made over muscles that can be used to address a wide range of conditions. It is suitable for skeletal, joint and muscle problems as well as for babies and children
Date Time.

If you are unable to keep your appointment, please contact us as soon as possible.

0417905368 ozmaisie@quellmail.net
Should not have
• Dont like times new roman and handwritten script font.

```html
<!DOCTYPE html>
<html lang="en">
<head>
<meta charset="utf-8">
<title>Maisie's Loxley Therapy – Business Card</title>
<link href="https://fonts.googleapis.com/css2?family=Questrial&display=swap" rel="stylesheet">
<style>
  :root {
    --page-bg: #e4e6e7;
    --card-white: #ffffff;
    --teal: #789da3;
    --name-panel: rgba(214, 226, 228, 0.72);
    --ink: #2a2d2e;
    --ink-soft: #4f5b5d;
  }
  * { margin: 0; padding: 0; box-sizing: border-box; }
  html, body {
    width: 1200px;
    height: 1000px;
    overflow: hidden;
    background: var(--page-bg);
    font-family: "Questrial", "Century Gothic", sans-serif;
  }
  .card {
    position: absolute;
    left: 110px;
    top: 210px;
    width: 980px;
    height: 580px;
    background: var(--card-white);
    overflow: hidden;
    box-shadow: 0 6px 24px rgba(0, 0, 0, 0.18);
  }
  .card__sweep {
    position: absolute;
    inset: 0;
    width: 100%;
    height: 100%;
  }
  .brand {
    position: absolute;
    left: 138px;
    top: 14px;
    color: var(--ink);
    white-space: nowrap;
  }
  .brand__name {
    font-size: 70px;
    font-weight: 400;
    letter-spacing: 0.5px;
    line-height: 1.1;
  }
  .brand__tagline {
    margin-left: 96px;
    margin-top: -4px;
    font-size: 29px;
    letter-spacing: 0.3px;
  }
  .practitioner {
    position: absolute;
    left: 458px;
    top: 196px;
    width: 372px;
    height: 106px;
    background: var(--name-panel);
    padding: 10px 0 0 28px;
    color: var(--ink);
    white-space: nowrap;
  }
  .practitioner__name {
    font-size: 44px;
    line-height: 1.1;
  }
  .practitioner__surname { color: var(--ink-soft); }
  .practitioner__role {
    margin-left: 8px;
    font-size: 24px;
    letter-spacing: 0.3px;
  }
  .contact {
    position: absolute;
    left: 46px;
    top: 340px;
    color: var(--ink);
    font-size: 29px;
    letter-spacing: 0.4px;
    list-style: none;
    white-space: nowrap;
  }
  .contact__item { line-height: 1; margin-bottom: 20px; }
  .contact__locations { line-height: 41px; margin-top: -4px; }
</style>
</head>
<body>
  <div class="card">
    <svg class="card__sweep" viewBox="0 0 980 580" aria-hidden="true">
      <path d="M22 0 C120 290, 460 500, 980 540 L980 0 Z" fill="var(--teal)"/>
      <path d="M45 0 C140 275, 470 478, 980 516" fill="none" stroke="var(--card-white)" stroke-width="5"/>
    </svg>

    <div class="brand">
      <h1 class="brand__name">Maisie's Loxley Therapy</h1>
      <p class="brand__tagline">Gentle therapy restoring body balance.</p>
    </div>

    <div class="practitioner">
      <p class="practitioner__name">Maisie<span class="practitioner__surname">Corbett</span></p>
      <p class="practitioner__role">Bowen Therapist,Cert IV</p>
    </div>

    <ul class="contact">
      <li class="contact__item">0417905368</li>
      <li class="contact__item">ozmaisie@quellmail.net</li>
      <li class="contact__item contact__locations">Lumacore Ashcombe<br>West Harrow Bay<br>Kelverton</li>
    </ul>
  </div>
</body>
</html>
```